International oil and gas consultancy business needs a web design

Hello, I need a web design for a new oil and gas auditing consultancy business. My business undertakes contract audit assignments to review past costs of oil and gas operations (see attached Excel file for more details of the businesses services). I need the design to give the impression of a professional consultancy style of business, rather than a retail style of website. Note: this job is for LAYOUT DESIGN ONLY and not coding / development work.
The following are my key design principles:
1. BASIC DESIGN: I am after a simple and static web design. I don't want the pages busy or cluttered with too many images or detail.
2. HORIZONTAL TABS: I require a horizontal set of tabs towards the top of the screens (see Excel file) which remain in the same position on every page.
3. META TAG PLANNING: The design should allow for effective positioning of content so that key meta tag words can easily be built during the technical build stage.
4. NUMBER OF PAGES: The site will eventually have a maximum of 10 pages. Seven of the pages will reside under the tabs. Can you please present your opening submission for the first two page.
5. USE OF MY LOGO: The attached logo (JPEG file) should be used throughout the website. Please don't change the shape and colour.
6. COLOUR SCHEMES: Can you please consider any of the 3 colour schemes below:
A - dark red (to match the logo), light grey and perhaps another of your liking;
B - dark red (to match the logo), light cream and perhaps another of your liking;
C - dark red (to match the logo), white and perhaps another of your liking.
7. WORD CONTENT: I have attached an Excel file which shows the estimated word content for each page.
8. FUTURE USE OF DESIGN: I'm planning on building a Wordpress website. Can you please ensure the layout design supports this application.

Target Market(s)

oil and gas companies (small and large)

Industry/Entity Type

Oil And Gas

Font styles to use
Sans Serif

Requirements
Nice to have
• The KOR logo and business name should ideally be next to each other. Also, the logo and name should be part of the background graphics, not above it.

```html
<!DOCTYPE html>
<html lang="en">
<head>
<meta charset="utf-8">
<title>Kestrel Oilfield Review</title>
<link rel="stylesheet" href="https://fonts.googleapis.com/css2?family=Open+Sans:wght@400;600;700&family=Quicksand:wght@500;600&display=swap">
<style>
:root{
  --brand-red:#8e1b1f;
  --ink:#333;
  --navy:#2f3140;
  --panel:#f3f3f3;
  --footer:#6a6f74;
  --footer-dark:#3a3c4a;
  --white:#fff;
  --logo-grey:#c9c9c9;
}
*{box-sizing:border-box;margin:0;padding:0}
html,body{width:898px;height:1200px;overflow:hidden;background:var(--white)}
body{position:relative;font-family:"Open Sans",sans-serif;color:var(--ink)}
.abs{position:absolute}

.brand{left:92px;top:8px;display:flex;flex-direction:column;align-items:center;width:152px}
.brand-mark{display:flex;align-items:center;gap:8px;color:var(--brand-red);font-weight:700;font-size:30px;letter-spacing:2px;line-height:1}
.brand-mark span.dot{width:14px;height:14px;background:var(--brand-red)}
.brand-name{margin-top:8px;color:var(--brand-red);font-size:9.5px;letter-spacing:2px}

.main-nav{right:90px;top:34px;display:flex;gap:21px;font-size:8.6px;text-transform:uppercase;color:#222}

.hero{left:90px;top:76px;width:718px;height:280px;background:linear-gradient(180deg,#3f7fc0 0%,#6ea3d4 45%,#3d6f9a 62%,#1c4873 100%)}
.hero-caption{left:33px;top:196px;font-family:"Quicksand",sans-serif;font-weight:600;color:var(--white);font-size:21px;line-height:33px}
.hero-arrow{top:128px;width:26px;height:26px;background:rgba(60,70,80,.55);display:flex;align-items:center;justify-content:center}

h2.section-title{font-weight:400;font-size:15px;color:var(--brand-red);text-transform:uppercase}
.lead{color:var(--brand-red);font-size:11px;line-height:17px}
.body-copy{font-size:8.4px;line-height:17px;color:#333}
.btn{display:inline-block;background:var(--navy);color:var(--white);font-size:8.6px;height:25px;line-height:25px;padding:0 14px;text-transform:uppercase}

.about{left:90px;top:380px;width:270px}
.why{left:387px;top:380px;width:420px}

.services{left:89px;top:577px;width:718px;height:287px;background:var(--panel)}
.services h2{text-align:center;margin-top:15px}
.service-card{top:63px;width:193px;height:202px}
.service-photo{width:193px;height:174px}
.service-bar{height:28px;background:var(--navy);color:var(--white);font-size:11.2px;line-height:28px;padding-left:9px;text-transform:uppercase;display:flex;align-items:center;gap:6px}

.partners{left:90px;top:888px;width:718px}
.partners h2{text-align:center}
.partner-row{display:flex;justify-content:center;gap:22px;margin-top:26px;align-items:center}
.partner-badge{width:88px;height:30px;background:#d8d8d8;border-radius:4px}

.site-footer{left:89px;top:1014px;width:719px;height:142px;background:var(--footer);color:var(--white)}
.foot-col{top:16px;display:flex;flex-direction:column;gap:10px;font-size:8.4px;font-weight:700;text-transform:uppercase}
.foot-label{font-size:8.4px;font-weight:700;text-transform:uppercase}
.social{display:flex;gap:10px}
.social span{width:28px;height:28px;border-radius:50%;background:#c8cacc}
.email{width:157px;height:24px;background:var(--white);color:#777;font-size:8px;line-height:24px;padding-left:8px;text-transform:uppercase}
.subscribe{height:25px;background:var(--navy);font-size:8.6px;line-height:25px;padding:0 12px;text-transform:uppercase;border-radius:2px}
.legal{left:89px;top:1156px;width:719px;height:26px;background:var(--footer-dark);color:var(--white);font-size:8.4px;line-height:26px;padding-left:13px}
</style>
</head>
<body>

<header>
  <div class="brand abs">
    <div class="brand-mark"><span class="dot"></span>KOR</div>
    <div class="brand-name">Kestrel Oilfield Review</div>
  </div>
  <nav class="main-nav abs">
    <span>Home</span><span>About Us</span><span>Services</span><span>Our Partners</span><span>Approach</span><span>Why Choose Us</span><span>Contact Us</span>
  </nav>
</header>

<section class="hero abs" role="img" aria-label="Offshore oil platforms with gas flares over a blue sea">
  <div class="hero-arrow abs" style="left:0">
    <svg width="10" height="14" viewBox="0 0 10 14"><path d="M8 1 2 7l6 6" fill="none" stroke="#fff" stroke-width="1.5"/></svg>
  </div>
  <div class="hero-arrow abs" style="right:0">
    <svg width="10" height="14" viewBox="0 0 10 14"><path d="M2 1l6 6-6 6" fill="none" stroke="#fff" stroke-width="1.5"/></svg>
  </div>
  <div class="hero-caption abs">Proin gravida nibh vel velit auctor aliquet<br>Aenean sollicitudin, lorem quis</div>
</section>

<section class="about abs">
  <h2 class="section-title">About Us</h2>
  <p class="body-copy" style="margin-top:14px"><span class="lead">Kestrel Oilfield Review</span> is a Perth (Australia) based firm specialising in providing quality audit services for the oil and gas industry.<br>Our skills and knowledge of oil and gas, along with a deep understanding of business commercial needs, ensures the high quality of our services</p>
  <span class="btn" style="margin-top:14px">Read More</span>
</section>

<section class="why abs">
  <h2 class="section-title" style="margin-left:2px">Why Choose Us</h2>
  <p class="lead" style="margin-top:12px">Proin gravida nibh vel velit auctor aliquet. Aenean sollicitudinrem quis bibendum auctor, nisi elit consequat ipsum, nec sagittis sem nibh id elit.</p>
  <p class="body-copy" style="margin-top:10px">Proin gravida nibh vel velit auctor aliquet. Aenean sollicitudinrem quis bibendum auctor, nisi elit consequat ipsum, nec sagittis sem nibh id elit. Duis sed odio sit amet nibh vulputate cursus a sit amet mauris. orbi accumsan ipsum velit.</p>
  <span class="btn" style="margin-top:14px">Read More</span>
</section>

<section class="services abs">
  <h2 class="section-title">Our Services</h2>
  <div class="service-card abs" style="left:33px">
    <div class="service-photo" role="img" aria-label="Oil pump jack under a blue sky" style="background:linear-gradient(180deg,#3f72b8 0%,#8fb3dc 60%,#6d7a4a 100%)"></div>
    <div class="service-bar">Joint Venture Audits <svg width="7" height="10" viewBox="0 0 7 10"><path d="M1 1l4 4-4 4" fill="none" stroke="#fff" stroke-width="1.8"/></svg></div>
  </div>
  <div class="service-card abs" style="left:262px">
    <div class="service-photo" role="img" aria-label="Engineers in hard hats reviewing plans beside pipework" style="background:linear-gradient(180deg,#7fa6d4 0%,#a7b4c2 45%,#2e3550 100%)"></div>
    <div class="service-bar">Contract Audits <svg width="7" height="10" viewBox="0 0 7 10"><path d="M1 1l4 4-4 4" fill="none" stroke="#fff" stroke-width="1.8"/></svg></div>
  </div>
  <div class="service-card abs" style="left:491px">
    <div class="service-photo" role="img" aria-label="Yellow oil pump jacks against a clear sky" style="background:linear-gradient(180deg,#2f6fb0 0%,#78a8d8 55%,#8b7d4a 100%)"></div>
    <div class="service-bar">Operations Audits <svg width="7" height="10" viewBox="0 0 7 10"><path d="M1 1l4 4-4 4" fill="none" stroke="#fff" stroke-width="1.8"/></svg></div>
  </div>
</section>

<section class="partners abs">
  <h2 class="section-title">Our Partners</h2>
  <div class="partner-row">
    <span class="partner-badge"></span><span class="partner-badge"></span><span class="partner-badge"></span><span class="partner-badge"></span><span class="partner-badge"></span><span class="partner-badge"></span>
  </div>
</section>

<footer class="site-footer abs">
  <div class="foot-col abs" style="left:15px"><span>Quick Link</span><span>About Us</span><span>Services</span><span>FAQs</span><span>Contacts</span></div>
  <div class="foot-col abs" style="left:163px"><span>Quick Link</span><span>Link Here</span><span>Reviews</span><span>News</span><span>Link Here</span></div>
  <div class="foot-col abs" style="left:298px"><span>Quick Link</span><span>Link Here</span><span>Link Here</span><span>Link Here</span><span>Link Here</span></div>
  <div class="foot-label abs" style="left:457px;top:17px">Connect With Us</div>
  <div class="social abs" style="left:457px;top:42px"><span></span><span></span><span></span><span></span><span></span><span></span></div>
  <div class="foot-label abs" style="left:457px;top:86px">Join Our Mailing List</div>
  <div class="email abs" style="left:457px;top:106px">Enter your email</div>
  <div class="subscribe abs" style="left:621px;top:106px">Subscribe</div>
</footer>
<div class="legal abs">Copyright © 2014 Kestrel Oilfield Review &nbsp;| Terms and Conditions | Privacy policy</div>

</body>
</html>
```